1. Overview of company:
Copper Lark Mobile solutions private Ltd is one of the leading innovators & providers of Value added services (VAS) and telecom solutions to the top telecom operators across the world. We are the pioneer of several telecom technologies and products with our solutions empowering over 40 telecom giant in 51 countries.

2. Product Overview:
Tonebender is the most innovative voice morphing mobile app that has revolutionized the concept of IVR based offerings for telecom operators across the world. It lets you talk to your friend in a voice of your choice at just the press of a button. In addition to every call, users can now speak to their friends with background sounds of their choice.

In simple words: If person A calls person B, person A can choose the voice he wants B to listen, Words and sentences remain same just the voice changes. Person A can even activate a background sound for both of them while talking.

3. Objective of the design:
The purpose of this campaign is to establish Tonebender as Innovative, Lively, Youthful, Fun mobile app generally used for spreading smiles via pranks. The primary objective is to persuade the audience to download and use Warblewick mobile app, as well as to spread and characterize this new app.

4. Product layout:
Page 1: Landing Page
- pictorial explanation, what Warblewick stands for

Page 2: Home Screen options
-Navigation to tonebender
-Navigation to sound canvas

Page 3: Warblewick options
-Female
-Cartoon
-King
-Bunny

Page 4: Sound Canvas options
-Romantic
-Airport
-Traffic
-Football
-Church
-Beach

5. Target Audience
The users of the mobile app will be teenager whose age ranges from 16-27. The demographics are not restricted to a particular country and will be present on global level.

6. Deliverable
- 4 Uncoded screen and icon for mobile app "Warblewick"
- Our company name is "Copper Lark" , we would like to see designs that use Black and Green, at the same time its not mandatory.
-Design should communicate what the app stands for "Changing voice of caller"

Target Market(s)

User of the mobile app will be teenagers whose age ranges from 16-27. The demographics are not restricted to a particular country and will be present on global level. It's for masses.

Industry/Entity Type

Telecommunications

Requirements
Must have
• The design should be self explanatory, what the app stands for.
• Editable format for integration purpose.
Nice to have
• Would prefer Icons and very few words.
• Professional, elegant at the same time trendy designs.

```html
<!DOCTYPE html>
<html lang="en">
<head>
<meta charset="utf-8">
<title>Warblewick options</title>
<link rel="stylesheet" href="https://fonts.googleapis.com/css2?family=Patrick+Hand&family=Roboto:wght@400;500&display=swap">
<style>
  :root {
    --stage: #e6e4e0;
    --screen: #ededed;
    --green: #8cc63f;
    --band: #dcdcdc;
    --band-text: #9a9a9a;
    --ink: #333333;
    --rule: #bdbdbd;
    --white: #ffffff;
    --orange: #e8a23a;
    --charcoal: #2f2f2f;
    --pink: #f3c3cf;
  }
  * { box-sizing: border-box; margin: 0; padding: 0; }
  html, body { width: 1200px; height: 1000px; overflow: hidden; }
  body { background: var(--stage); position: relative; }

  .app-screen {
    position: absolute; left: 360px; top: 74px;
    width: 480px; height: 852px;
    background: var(--screen);
    overflow: hidden;
    box-shadow: 0 6px 24px rgba(0,0,0,0.12);
  }

  .status-bar {
    height: 30px; background: var(--green);
    display: flex; align-items: center; justify-content: space-between;
    padding: 0 14px;
    font-family: "Roboto", sans-serif; font-size: 14px; color: var(--white);
  }
  .status-bar .signal { letter-spacing: 1px; font-size: 12px; }
  .status-bar .battery { display: flex; align-items: center; gap: 6px; }
  .battery-icon { width: 26px; height: 12px; border: 1.5px solid var(--white); border-radius: 2px; padding: 1px; }
  .battery-icon span { display: block; width: 100%; height: 100%; background: var(--white); }

  .title-bar {
    height: 72px; background: var(--green);
    position: relative; display: flex; align-items: center; justify-content: center;
  }
  .title-bar .back { position: absolute; left: 22px; top: 24px; }
  .title-bar h1 {
    font-family: "Patrick Hand", cursive; font-weight: 400;
    font-size: 32px; color: var(--white); letter-spacing: 1px;
  }

  .hint-band {
    height: 30px; background: var(--band);
    font-family: "Roboto", sans-serif; font-size: 14px; color: var(--band-text);
    display: flex; align-items: center; justify-content: center;
  }

  .voice-list { list-style: none; margin-top: 56px; padding: 0 20px 0 28px; }
  .voice-option {
    height: 86px; display: flex; align-items: center;
    padding: 0 20px 0 12px; border-bottom: 1.5px solid var(--rule);
  }
  .voice-option:last-child { border-bottom: none; }
  .voice-icon { width: 56px; height: 50px; border-radius: 10px; flex: none; }
  .voice-icon.female { background: var(--orange); border-radius: 50% 50% 12px 12px; }
  .voice-icon.cartoon { background: var(--charcoal); border-radius: 50%; }
  .voice-icon.king { background: var(--orange); height: 36px; }
  .voice-icon.bunny { background: var(--pink); height: 40px; border-radius: 50% 50% 8px 8px; }
  .voice-name {
    font-family: "Patrick Hand", cursive; font-size: 32px; color: var(--ink);
    margin-left: 22px; flex: 1;
  }
  .radio {
    width: 24px; height: 24px; border-radius: 50%;
    border: 2px solid var(--green); position: relative; flex: none;
  }
  .radio.selected::after {
    content: ""; position: absolute; inset: 3px;
    border-radius: 50%; background: var(--green);
  }

  .save-button {
    position: absolute; left: 175px; top: 716px;
    width: 136px; height: 52px;
    background: var(--green); color: var(--white);
    font-family: "Patrick Hand", cursive; font-size: 32px;
    display: flex; align-items: center; justify-content: center;
    transform: rotate(-3deg);
    border: none;
  }
</style>
</head>
<body>
  <main class="app-screen">
    <div class="status-bar">
      <span class="signal">●●●●●</span>
      <span class="clock">12:49 PM</span>
      <span class="battery">100% <span class="battery-icon"><span></span></span></span>
    </div>

    <header class="title-bar">
      <svg class="back" width="16" height="24" viewBox="0 0 16 24" aria-label="Back">
        <polyline points="13,3 4,12 13,21" fill="none" stroke="#ffffff" stroke-width="3" stroke-linecap="round" stroke-linejoin="round"/>
      </svg>
      <h1>Warblewick options</h1>
    </header>

    <div class="hint-band">select the voice that you want to talk</div>

    <ul class="voice-list">
      <li class="voice-option">
        <div class="voice-icon female" role="img" aria-label="Female voice illustration"></div>
        <span class="voice-name">Female</span>
        <span class="radio"></span>
      </li>
      <li class="voice-option">
        <div class="voice-icon cartoon" role="img" aria-label="Cartoon voice character illustration"></div>
        <span class="voice-name">Cartoon</span>
        <span class="radio selected"></span>
      </li>
      <li class="voice-option">
        <div class="voice-icon king" role="img" aria-label="King voice crown illustration"></div>
        <span class="voice-name">King</span>
        <span class="radio"></span>
      </li>
      <li class="voice-option">
        <div class="voice-icon bunny" role="img" aria-label="Bunny voice ears illustration"></div>
        <span class="voice-name">Bunny</span>
        <span class="radio"></span>
      </li>
    </ul>

    <button class="save-button">SAVE</button>
  </main>
</body>
</html>
```